Business Card Design Project

My business sells promotional merchandise to large blue chip companies. Gear like polo shirts, drink bottles, pens, basically anything that you can put a company logo onto.

I need the following elements included:
Logo as attached
Peter Hollingdale Managing Director
27 Corbel Street Tarrin Cove 4178
mobile 0438 514203
email kestrelpath@kestrelpathtrading.com.au

Branded Merchandise with Real Character

Target Market(s)

Mature age Marketing Managers

Industry/Entity Type

Business

```html
<!DOCTYPE html>
<html lang="en">
<head>
<meta charset="utf-8">
<title>Kestrelpath Business Card</title>
<link rel="stylesheet" href="https://fonts.googleapis.com/css2?family=Questrial&family=Arimo:wght@400&display=swap">
<style>
  :root {
    --stage: #d6dbda;
    --royal: #1f36e6;
    --royal-deep: #1424b8;
    --royal-light: #4a6bff;
    --brand-blue: #2a3fe0;
    --ink: #1c1c1c;
    --paper: #ffffff;
    --mist: #e4e7ea;
  }
  * { margin: 0; padding: 0; box-sizing: border-box; }
  html, body { width: 1200px; height: 357px; overflow: hidden; background: var(--stage); }
  .canvas { position: relative; width: 1200px; height: 357px; }

  .card { position: absolute; top: 11px; height: 335px; overflow: hidden; background: var(--paper); }

  /* Front */
  .card-front { left: 9px; width: 586px; }
  .front-field {
    position: absolute; left: 0; top: 0; width: 100%; height: 290px;
    background: linear-gradient(135deg, var(--royal-deep) 0%, var(--royal) 45%, var(--royal-light) 70%, var(--royal) 100%);
  }
  .front-wordmark {
    position: absolute; left: 0; width: 100%; top: 102px; text-align: center;
    font-family: "Questrial", sans-serif; font-size: 52px; line-height: 60px; letter-spacing: 1px;
    color: var(--paper);
  }
  .front-web {
    position: absolute; left: 0; width: 100%; top: 184px; text-align: center;
    font-family: "Questrial", sans-serif; font-size: 15px; line-height: 18px; letter-spacing: 2.2px;
    color: var(--paper);
  }
  .tagline {
    position: absolute; left: 0; width: 100%; top: 305px; text-align: center;
    font-family: "Arimo", sans-serif; font-size: 16px; line-height: 18px; text-transform: uppercase;
    color: var(--brand-blue);
  }

  /* Back */
  .card-back {
    left: 605px; width: 585px;
    background: radial-gradient(ellipse 60% 70% at 50% 45%, var(--mist) 0%, var(--paper) 80%);
  }
  .back-wordmark {
    position: absolute; left: 31px; top: 135px;
    font-family: "Questrial", sans-serif; font-size: 33px; line-height: 40px; letter-spacing: 0.5px;
    color: var(--brand-blue);
  }
  .accent-bar {
    position: absolute; left: 266px; top: 136px; width: 252px; height: 24px;
    background: linear-gradient(90deg, var(--brand-blue) 0%, var(--brand-blue) 20%, rgba(42,63,224,0) 100%);
  }
  .person { position: absolute; right: 57px; top: 83px; text-align: right; }
  .person-name { font-family: "Arimo", sans-serif; font-size: 27px; color: var(--brand-blue); line-height: 1.05; }
  .person-role { font-family: "Arimo", sans-serif; font-size: 14px; color: var(--ink); margin-top: 1px; }

  .contact { position: absolute; left: 280px; top: 172px; font-family: "Arimo", sans-serif; font-size: 13.5px; color: var(--ink); }
  .contact li { list-style: none; height: 17.5px; display: flex; align-items: center; gap: 4px; white-space: nowrap; }
  .contact svg { width: 13px; height: 11px; fill: var(--ink); flex: none; }

  .back-web {
    position: absolute; left: 0; width: 100%; top: 289px; text-align: center;
    font-family: "Questrial", sans-serif; font-size: 15.5px; line-height: 18px; letter-spacing: 2.6px;
    color: var(--brand-blue);
  }
</style>
</head>
<body>
<main class="canvas">
  <section class="card card-front">
    <div class="front-field" role="img" aria-label="Royal blue field with soft diagonal light streaks"></div>
    <div class="front-wordmark">KESTRELPATH</div>
    <div class="front-web">www.kestrelpathtrading.com.au</div>
    <div class="tagline">Branded Merchandise with Real Character</div>
  </section>

  <section class="card card-back">
    <div class="person">
      <div class="person-name">Peter Hollingdale</div>
      <div class="person-role">Managing Director</div>
    </div>
    <div class="back-wordmark">KESTRELPATH</div>
    <div class="accent-bar"></div>
    <ul class="contact">
      <li>27 Corbel Street Tarrin Cove 4178</li>
      <li>
        <svg viewBox="0 0 13 11" aria-hidden="true"><path d="M1 3 Q6.5 -0.5 12 3 L10.5 4.5 L9 3.5 L4 3.5 L2.5 4.5 Z"/><rect x="2.5" y="5" width="8" height="5.5" rx="1"/></svg>
        0438 514203
      </li>
      <li>
        <svg viewBox="0 0 13 11" aria-hidden="true"><rect x="0.5" y="1.5" width="12" height="8" rx="0.5"/><path d="M1 2 L6.5 6.5 L12 2" fill="none" stroke="#fff" stroke-width="1.2"/></svg>
        kestrelpath@kestrelpathtrading.com.au
      </li>
    </ul>
    <div class="back-web">www.kestrelpathtrading.com.au</div>
  </section>
</main>
</body>
</html>
```